Briefpapier und Visitenkarten
Zielgruppe
Das Design soll Herren im mittleren bis hohen Alter ansprechen.
Aufgabenstellung
Benötigt wird ein Briefpapier für die Koresspondenz und die Rechnungen. Ein Logo ist vorhanden und muss ins Briefpapier und auf die Visitenkarten einbebunden werden.

```html
<!DOCTYPE html>
<html lang="de">
<head>
<meta charset="utf-8">
<title>nordlicht data – Visitenkarte</title>
<link href="https://fonts.googleapis.com/css2?family=Arimo:wght@400;700&display=swap" rel="stylesheet">
<style>
  :root {
    --stage: #45545b;
    --paper: #ffffff;
    --ink: #111111;
    --night: #0c0d10;
    --brand-red: #c4122f;
    --text-light: #ffffff;
  }
  * { margin: 0; padding: 0; box-sizing: border-box; }
  html, body {
    width: 1200px; height: 572px; overflow: hidden;
    background: var(--stage);
    font-family: "Arimo", Arial, sans-serif;
  }
  .stage { position: relative; width: 1200px; height: 572px; }

  .card {
    position: absolute;
    width: 418px; height: 270px;
    overflow: hidden;
    box-shadow: 0 3px 10px rgba(0,0,0,.35);
  }

  /* Vorderseite */
  .card--front { left: 62px; top: 59px; background: var(--paper); }
  .card__swoosh { position: absolute; inset: 0; width: 418px; height: 270px; }

  .wordmark {
    position: absolute;
    display: flex; align-items: center; gap: 6px;
    color: var(--brand-red);
    font-weight: 400;
    white-space: nowrap;
  }
  .wordmark__dot { border-radius: 50%; background: var(--brand-red); flex: none; }

  .card--front .wordmark { left: 17px; top: 18px; font-size: 21px; }
  .card--front .wordmark__dot { width: 12px; height: 12px; }

  .contact { position: absolute; left: 17px; color: var(--ink); white-space: nowrap; }
  .contact__name, .contact__role { font-weight: 700; font-size: 11px; line-height: 15px; }
  .contact__name { top: 81px; }
  .contact__role { top: 97px; }
  .contact__street { top: 128px; font-size: 10.5px; line-height: 14px; }
  .contact__city { top: 144px; font-size: 10.5px; line-height: 14px; }
  .contact__phone { font-size: 9px; line-height: 12px; }
  .contact__phone--tel { top: 170px; }
  .contact__phone--fax { top: 184px; }
  .contact__phone--mobil { top: 199px; }

  .web {
    position: absolute; right: 11px; top: 236px;
    color: var(--text-light);
    font-size: 10.5px; line-height: 13px; text-align: right;
  }

  /* Rückseite */
  .card--back {
    left: 648px; top: 199px;
    background: var(--night);
    display: flex; align-items: center; justify-content: center;
  }
  .card--back .wordmark { position: static; font-size: 38px; gap: 10px; }
  .card--back .wordmark__dot { width: 22px; height: 22px; }
</style>
</head>
<body>
<main class="stage">

  <section class="card card--front" aria-label="Visitenkarte Vorderseite">
    <svg class="card__swoosh" viewBox="0 0 418 270" aria-hidden="true">
      <path d="M0 226 C 150 226, 300 206, 418 168 L418 270 L0 270 Z" fill="var(--brand-red)"/>
      <path d="M0 233 C 160 233, 310 214, 418 179 L418 270 L0 270 Z" fill="var(--night)"/>
    </svg>

    <div class="wordmark"><span>nordlicht</span><span class="wordmark__dot"></span><span>data</span></div>

    <p class="contact contact__name">Max Mustermann</p>
    <p class="contact contact__role">Senior Project Manager</p>
    <p class="contact contact__street">Musterstraße 34</p>
    <p class="contact contact__city">75364 Musterhausen</p>
    <p class="contact contact__phone contact__phone--tel">Tel 0123 / 456 789</p>
    <p class="contact contact__phone contact__phone--fax">Fax 0123 / 46 789</p>
    <p class="contact contact__phone contact__phone--mobil">Mobil 0177 / 645 345 45</p>

    <p class="web">info@nordlichtdata.de<br>www.nordlichtdata.de</p>
  </section>

  <section class="card card--back" aria-label="Visitenkarte Rückseite">
    <div class="wordmark"><span>nordlicht</span><span class="wordmark__dot"></span><span>data</span></div>
  </section>

</main>
</body>
</html>
```